App Design Project

We are building an app and looking for design help on an existing template. We will also need a style guide. For more information, there is a website which outlines the assignment with visuals. Go here:

http://www.brivolane.com/

Industry/Entity Type

Building

```html
<!DOCTYPE html>
<html lang="en">
<head>
<meta charset="utf-8">
<title>Brivolane – Splash Screen</title>
<link rel="stylesheet" href="https://fonts.googleapis.com/css2?family=Open+Sans:wght@600;700&display=swap">
<style>
  :root {
    --page-bg: #0a141c;
    --screen-top: #082a40;
    --screen-mid: #0d4764;
    --screen-bottom: #0a3550;
    --streak: rgba(120, 200, 235, 0.07);
    --horizon: rgba(150, 225, 255, 0.35);
    --brand-white: #ffffff;
    --tagline-cyan: #1de6f2;
    --emblem-light: #e4e7e9;
    --emblem-dark: #8e969b;
    --map-glow: #bff3ff;
    --map-deep: #2a8fb5;
  }

  * { box-sizing: border-box; margin: 0; padding: 0; }

  html, body {
    width: 1200px;
    height: 2345px;
    overflow: hidden;
    background: var(--page-bg);
  }

  .splash-screen {
    position: absolute;
    left: 0;
    top: 311px;
    width: 1200px;
    height: 1722px;
    overflow: hidden;
    background:
      repeating-linear-gradient(90deg, transparent 0 38px, var(--streak) 38px 44px, transparent 44px 97px),
      radial-gradient(ellipse 55% 30% at 50% 62%, rgba(120, 210, 245, 0.35), transparent 70%),
      linear-gradient(180deg, var(--screen-top) 0%, var(--screen-mid) 48%, var(--screen-bottom) 100%);
  }

  .brand-emblem {
    position: absolute;
    left: 386px;
    top: 126px;
    width: 440px;
    height: 440px;
    border-radius: 50%;
    background: radial-gradient(circle at 40% 35%, var(--emblem-light) 0%, #b9bfc3 55%, var(--emblem-dark) 100%);
  }

  .brand-name {
    position: absolute;
    left: 0;
    width: 100%;
    top: 660px;
    text-align: center;
    font-family: "Open Sans", sans-serif;
    font-weight: 600;
    font-size: 190px;
    line-height: 1;
    letter-spacing: 4px;
    color: var(--brand-white);
  }

  .tagline {
    position: absolute;
    left: 0;
    width: 100%;
    top: 884px;
    text-align: center;
    font-family: "Open Sans", sans-serif;
    font-weight: 700;
    font-size: 58px;
    line-height: 1;
    letter-spacing: 1px;
    color: var(--tagline-cyan);
  }

  .horizon-line {
    position: absolute;
    left: 0;
    top: 972px;
    width: 100%;
    height: 3px;
    background: linear-gradient(90deg, transparent, var(--horizon) 30%, var(--horizon) 70%, transparent);
  }

  .world-map {
    position: absolute;
    left: 58px;
    top: 990px;
    width: 1095px;
    height: 508px;
    border-radius: 40px;
    background: radial-gradient(ellipse 60% 60% at 50% 45%, var(--map-glow) 0%, rgba(110, 205, 235, 0.55) 45%, rgba(42, 143, 181, 0) 80%);
  }
</style>
</head>
<body>
  <main class="splash-screen">
    <div class="brand-emblem" aria-hidden="true"></div>
    <h1 class="brand-name">Brivolane</h1>
    <p class="tagline">TRAVEL. CONNECT. PLAY</p>
    <div class="horizon-line" aria-hidden="true"></div>
    <div class="world-map" role="img" aria-label="Glowing dotted world map of the continents"></div>
  </main>
</body>
</html>
```